Zielgruppe
Ich zeige Frauen 35+ wie sie ihren Traummann finden können, ohne im Internet nach ihm zu suchen. Meine Zielgruppe sind meist Frauen, die schon lange Single sind und doch voller Sehnsucht nach einem Partner. Diese Frauen haben oft negative Erfolgsverhinderer-Glaubenssätze ('In meinem Alter gibt es keine guten Männer mehr', 'Ich bin zu dick - Männer wollen schlanke Frauen'...). Ich zeige diesen Frauen, wie sie durch eine andere Einstellung in kurzer Zeit ihren Herzenspartner ins Leben ziehen können.
Aufgabenstellung
Die Menschen, die dieses Buch lesen, sind normalerweise weiblich und mindestens 35 Jahre alt, eher älter. Das Cover sollte also Frauen ansprechen, die sich ihren Traummann wünschen und darf gerne auch 'weibliche' Farbtöne wie rot und rosa, pink etc. enthalten (das sind auch 'meine' Business-Farben). Es ist aber nur eine Idee von mir, keine Vorgabe. Ich bin offen für alles.

```html
<!DOCTYPE html>
<html lang="de">
<head>
<meta charset="utf-8">
<title>Wer loslassen kann, der gewinnt – Buchcover</title>
<link rel="stylesheet" href="https://fonts.googleapis.com/css2?family=Mrs+Saint+Delafield&family=Josefin+Sans:wght@300;700&display=swap">
<style>
  :root {
    --wine: #6f0d1a;
    --white: #ffffff;
    --blush: #f2c3c0;
    --rose: #e98c97;
    --skin: #c98a78;
    --pale: #f4e6d6;
    --brand: #7a1020;
    --brand-dot: #e5202e;
  }
  html, body {
    margin: 0;
    padding: 0;
    width: 752px;
    height: 1200px;
    overflow: hidden;
    background: var(--wine);
  }
  .cover {
    position: relative;
    width: 752px;
    height: 1200px;
    overflow: hidden;
    background: var(--wine);
  }
  .cover-photo {
    position: absolute;
    left: 0;
    top: 0;
    width: 752px;
    height: 630px;
    background:
      radial-gradient(ellipse 260px 200px at 380px 280px, var(--pale) 0%, rgba(244,230,214,0) 100%),
      radial-gradient(ellipse 300px 260px at 120px 300px, var(--skin) 0%, rgba(201,138,120,0) 100%),
      radial-gradient(ellipse 260px 320px at 640px 320px, #d9a08f 0%, rgba(217,160,143,0) 100%),
      radial-gradient(ellipse 200px 160px at 340px 390px, var(--rose) 0%, rgba(233,140,151,0) 100%),
      linear-gradient(180deg, var(--blush) 0%, #efb7b4 60%, #e8a6ab 100%);
  }
  .cover-wave {
    position: absolute;
    left: 0;
    top: 560px;
    width: 752px;
    height: 80px;
    display: block;
  }
  .brand {
    position: absolute;
    left: 578px;
    top: 520px;
    display: flex;
    align-items: center;
    gap: 6px;
    font-family: "Josefin Sans", sans-serif;
    font-weight: 700;
    font-size: 24px;
    color: var(--brand);
  }
  .brand-dot {
    width: 12px;
    height: 12px;
    border-radius: 50%;
    background: var(--brand-dot);
  }
  .title {
    position: absolute;
    left: 0;
    top: 682px;
    width: 752px;
    margin: 0;
    text-align: center;
    font-family: "Mrs Saint Delafield", cursive;
    font-weight: 400;
    font-size: 122px;
    line-height: 96px;
    color: var(--white);
  }
  .subtitle {
    position: absolute;
    left: 0;
    top: 926px;
    width: 752px;
    margin: 0;
    text-align: center;
    font-family: "Josefin Sans", sans-serif;
    font-weight: 300;
    font-size: 37px;
    line-height: 54px;
    color: var(--white);
  }
  .author {
    position: absolute;
    left: 0;
    top: 1100px;
    width: 752px;
    margin: 0;
    text-align: center;
    font-family: "Josefin Sans", sans-serif;
    font-weight: 700;
    font-size: 34px;
    letter-spacing: 0.5px;
    color: var(--white);
  }
</style>
</head>
<body>
  <main class="cover">
    <div class="cover-photo" role="img" aria-label="Foto: zwei Hände formen ein Herz vor einem unscharfen, rosafarbenen Blumenhintergrund"></div>
    <svg class="cover-wave" viewBox="0 0 752 80" preserveAspectRatio="none" aria-hidden="true">
      <path d="M0 20 C 180 10, 420 20, 752 64 L 752 80 L 0 80 Z" fill="var(--wine)"/>
    </svg>
    <div class="brand"><span class="brand-dot"></span>amorelle</div>

    <h1 class="title">Wer loslassen kann,<br>der gewinnt</h1>
    <p class="subtitle">Warum du endlich aufhören<br>solltest, der Liebe nachzujagen</p>
    <p class="author">Mirela&nbsp; Kornthaler-Weiss</p>
  </main>
</body>
</html>
```